Website Redesign for a faith-based, not-for-profit health and human services organization

New website design for the Hearthside Faith Outreach House.
- Current site: www.hfohtr.org -
We are looking for a nice clean, simple, friendly-yet-elegant website layout.
Colors are #f5eed5 (cream), #FFFFFF (white), and all logo colors.
Design a layout for home page
Design a layout for general layouts
-layout only no html needed (preferably a high res PSD file format) -
Main menu should be along top with side navigation for submenu, no side menu on home page.
Also would be open to seeing some updated colors on the logo design, currently the colors are slightly outdated. The Vine of Plenty quilt design fits the organization’s mission and the rural farming / Amish-Mennonite-Brethren community around us.

ADDITIONAL PAGES AND MENU STRUCTURE ON NEW SITE

- How to Help
... Volunteer
... Donate Time
... Donate Money
... Donate Supplies
... Current Needs

- Programs

- News & Events
... Upcoming Events
... Upcoming Fundraisers
... Newsletter

- Our Partners

- About Us
... Overview
... Mission
... Staff Directory
... Board of Directors
... Annual Reports

- Contact

Our annual special event is Gather at the Hearth and should be integrated into the home page - see attached logos and banner

Websites with elements we like (from organizations doing similar work), each for a different reason....

1. http://www.kinbridgeway.org
Good design, color, clarity on this site. Multi-dimensional, photos...easy interaction, etc.

2. http://endfamineplainly.org
Quite simple, nothing fancy, but some good basic stuff here, and pretty easy to navigate...

3. http://www.neighborhub.org
Intrigued by the bulletin board design and the way they have their programs broken down to show impact, needs, etc. It has a lot of good information, but is really too verbose, some of the print is too small, etc. Not perfect, but some interesting design elements.

4. http://sharedlarder.org
Site is boring and not very well designed, but it has some of the features that we would like to see at the top, donations, partners, etc.

5. http://www.meadowlarkgrocers.org
Too many listings on the sidebar - needs to be cleaner & simpler, but a lot of good information and we like the way they show volunteer photos on the Our Helpers Shine Bright page...

About
Hearthside Faith Outreach House ("HFOH" or “the Center”) is a faith-based non-for-profit health and human services organization that exists as an outreach of and for the Ostrel Valley Unified School District.
Tagline: Mercy at Work (we work to serve the needs of the ‘least of these’ with compassion).

Mission
Our mission is to see lives transformed and the community enhanced by encouraging the oppressed, defending the cause of the weak and maintaining the rights of the poor - bringing together the resources of a caring community as a demonstration of the good news of Christ.

Company Overview
Hearthside Faith Outreach House works closely with the community in which it serves. A tremendous value is placed upon the partnerships that have formed with caring people within the community and with organizations that share the goal of bringing together resources to help those who need it most. Individuals, volunteers, churches, corporations, foundations, and government sources all pull together to help make our mission possible.

Since 1996 the Hearthside Faith Outreach House has collaboratively worked to see our community enhanced, adapting programs and services to meet the changing needs of the community.

Target Market(s)

people needing assistance in local community

Industry/Entity Type

Government

Requirements
Must have
• Good social button integration
Should not have
• No Find Us page like old website it is not needed

```html
<!DOCTYPE html>
<html lang="en">
<head>
<meta charset="utf-8">
<title>About Us – Hearthside Faith Outreach House</title>
<link rel="stylesheet" href="https://fonts.googleapis.com/css2?family=Open+Sans:wght@400;600;700&display=swap">
<style>
  :root {
    --wine: #7a1b2e;
    --forest: #1f3b2c;
    --ink: #222222;
    --paper: #f2f1ee;
    --cream: #f3ecd8;
    --gold: #c9a24a;
    --wood-dark: #3a2412;
    --wood-mid: #5c3a1e;
    --rule: #c9c6c0;
    --white: #ffffff;
  }
  * { box-sizing: border-box; margin: 0; padding: 0; }
  html, body { width: 776px; height: 1200px; overflow: hidden; }
  body {
    position: relative;
    font-family: "Open Sans", Arial, sans-serif;
    color: var(--ink);
    background: var(--paper);
  }

  /* Header */
  .site-header {
    position: absolute; left: 0; top: 0; width: 776px; height: 78px;
    background: var(--white);
  }
  .brand {
    position: absolute; left: 36px; top: 8px;
    display: flex; align-items: center; gap: 10px;
    text-decoration: none;
  }
  .brand-mark { width: 58px; height: 58px; background: var(--wine); }
  .brand-name {
    width: 110px;
    font-size: 13px; line-height: 14px; font-weight: 600;
    color: var(--forest);
  }
  .main-nav {
    position: absolute; right: 34px; top: 36px;
    display: flex; gap: 10px;
  }
  .main-nav a {
    font-size: 11.5px; font-weight: 600; text-transform: uppercase;
    color: var(--ink); text-decoration: none; letter-spacing: -0.1px;
  }
  .main-nav a.is-current { color: var(--wine); }
  .social { position: absolute; display: flex; gap: 8px; }
  .social span {
    display: block; width: 14px; height: 14px; border-radius: 50%;
    background: var(--ink);
  }
  .site-header .social { right: 34px; top: 10px; }

  /* Hero */
  .hero-band {
    position: absolute; left: 0; top: 78px; width: 776px; height: 264px;
    background: linear-gradient(90deg, var(--wood-dark), var(--wood-mid) 30%, var(--wood-dark) 55%, var(--wood-mid) 80%, var(--wood-dark));
    border-bottom: 4px solid var(--gold);
  }
  .hero-photo {
    position: absolute; left: 35px; top: 120px; width: 705px; height: 308px;
    border: 5px solid var(--white);
    background: linear-gradient(135deg, #7d8288, #a9adb2 45%, #d7d9dc 75%, #8e8a80);
    box-shadow: 0 1px 4px rgba(0,0,0,.3);
  }

  /* Sub navigation */
  .sub-nav {
    position: absolute; left: 35px; top: 480px; width: 167px;
    list-style: none;
    border-top: 1px dotted var(--rule);
  }
  .sub-nav li { border-bottom: 1px dotted var(--rule); }
  .sub-nav a {
    display: block; height: 32px; line-height: 32px; padding-left: 13px;
    font-size: 12px; text-transform: uppercase;
    color: var(--forest); text-decoration: none;
  }
  .sub-nav a.is-current { border-left: 3px solid var(--wine); padding-left: 10px; }
  .column-rule {
    position: absolute; left: 228px; top: 480px; width: 1px; height: 662px;
    background: #d2cfca;
  }

  /* Content */
  .content { position: absolute; left: 269px; top: 472px; width: 474px; }
  .page-title {
    font-size: 34px; font-weight: 700; color: var(--wine);
    text-transform: uppercase; letter-spacing: -0.5px; line-height: 44px;
  }
  .tagline {
    margin-top: 10px; height: 62px; padding: 8px 0 0 12px;
    border-left: 4px solid var(--wine);
    background: repeating-linear-gradient(45deg, rgba(0,0,0,.03) 0 2px, transparent 2px 5px);
  }
  .tagline h2 {
    font-size: 17px; font-weight: 600; color: var(--forest);
    text-transform: uppercase; line-height: 22px;
  }
  .tagline p { font-size: 13px; line-height: 18px; }
  .intro {
    margin-top: 28px; font-size: 12.6px; line-height: 20.5px;
  }
  .intro .org { color: var(--wine); }
  .feature-photo {
    margin-top: 31px; width: 474px; height: 226px;
    border: 5px solid var(--white);
    background: linear-gradient(180deg, #b9b4a9, #7e6a66 50%, #4b3f3c);
    box-shadow: 0 1px 4px rgba(0,0,0,.35);
  }

  /* Footer */
  .site-footer {
    position: absolute; left: 0; top: 1154px; width: 776px; height: 46px;
    background: var(--cream);
    border-top: 1px solid #e2d9bf;
  }
  .site-footer p {
    position: absolute; left: 26px; top: 15px;
    font-size: 10.6px; font-weight: 700; text-transform: uppercase;
  }
  .site-footer .org { color: var(--wine); }
  .site-footer .social { left: 510px; top: 16px; }
</style>
</head>
<body>
  <header class="site-header">
    <a class="brand" href="#">
      <span class="brand-mark"></span>
      <span class="brand-name">Hearthside Faith Outreach House</span>
    </a>
    <div class="social" aria-label="Social links"><span></span><span></span></div>
    <nav class="main-nav">
      <a href="#">Home</a>
      <a href="#" class="is-current">About Us</a>
      <a href="#">How to Help</a>
      <a href="#">Our Partners</a>
      <a href="#">News &amp; Events</a>
      <a href="#">Programs</a>
      <a href="#">Contact</a>
    </nav>
  </header>

  <div class="hero-band"></div>
  <div class="hero-photo" role="img" aria-label="Photo of a smiling volunteer carrying a cardboard box out of a supply trailer"></div>

  <ul class="sub-nav">
    <li><a href="#" class="is-current">Overview</a></li>
    <li><a href="#">Mission</a></li>
    <li><a href="#">Staff Directory</a></li>
    <li><a href="#">Board of Directors</a></li>
    <li><a href="#">Annual Reports</a></li>
  </ul>
  <div class="column-rule"></div>

  <main class="content">
    <h1 class="page-title">About Us</h1>
    <div class="tagline">
      <h2>Mercy at Work</h2>
      <p>We work to serve the needs of the ‘least of these’ with compassion.</p>
    </div>
    <p class="intro"><span class="org">Hearthside Faith Outreach House</span> ("HFOH" or “the Center”) is a faith-based non-for-profit health and human services organization that exists as an outreach of and for the Ostrel Valley Unified School District.</p>
    <div class="feature-photo" role="img" aria-label="Group photo of volunteers gathered around boxes of holiday gifts"></div>
  </main>

  <footer class="site-footer">
    <p>Copyright 2013 | <span class="org">Hearthside Faith Outreach House</span> | All Rights Reserved</p>
    <div class="social" aria-label="Social links"><span></span><span></span></div>
  </footer>
</body>
</html>
```